K P Guard Services - Alarm and CCTV installation Flyer

Need a flyer designed that grabs the attention of potential customers, we need the price to stand out the most to grab people’s attention, whether they are residential or commercial.We are a security company based in Brentwood Essex but cover London and the home counties. here is our website to take a look at www.kpguardservices.co.uk. We want them to know we install complete alarm and Cctv systems and will keep them “safe”

Target Market(s)

residential and commercial property

Colors
f37122

Requirements
Must have
• on one side
• large clear logo - professional design
• - Intruder Alarms starting from £495 + VAT. (Big text)
• - £150 discount on installations
• *terms and conditions apply (small text)
• - Not happy with your current provider? Free of charge no obligation take over survey and quotation and up to £100 off
• - CCTV systems starting from £595 + VAT (based on 2 cameras)
• K P Guard Services are always there, always available, wherever and whenever you need us.
• Large telephone number at the bottom 01632 480913
• Address / email / website as a footer * see website for details
• on second side
• large and bold
• Are you looking to keep you and your premises safe?
• - K P Guard Services install, maintain and repair all intruder alarms, CCTV, intercom and access control
• - View, control and manage your security systems anywhere in the world
• - Feel at ease with monitoring services & police response tailored to suit you and your business
• - K P Guard can takeover any existing security system and offer maintenance checks to guarantee the best performance for you and your premises
• - K P Guard understand that being security conscious is ever increasing, protecting your property and family is a number one priority
• - Our fully insured and accredited team offer quality, safety and cost efficiency throughout the whole process
• - K P Guard Services are using the latest cloud-based technology to stay connected with your home and business 24/7
• If you are looking to improve the security in your home, office or commercial property then call a member of our team today for a free quote.
• Fully insured and accredited
• Jobrater logo and NQRB Intruder and CCTV logos
• Logo somewhere on page and
• Telephone number
• Address / email / website as footer
Nice to have
• We would like to have the text saying
• Intruder alarms installed from £495 + vat the biggest text on the page. Most likely the £495 part the largest.
• Also would like “not happy with your current provider” more obvious
• We would like use our company colours - Orange/White/black

```html
<!DOCTYPE html>
<html lang="en">
<head>
<meta charset="utf-8">
<title>K P Guard Services – Alarm and CCTV Flyer</title>
<link href="https://fonts.googleapis.com/css2?family=Roboto:wght@300;400;500;700;900&family=Roboto+Condensed:wght@700&display=swap" rel="stylesheet">
<style>
  :root{
    --red:#d71f26;
    --red-dark:#a9151b;
    --black:#111111;
    --ink:#1d1d1d;
    --yellow:#ffd200;
    --white:#ffffff;
    --grey:#6b6b6b;
    --page:#e9e9e9;
  }
  *{box-sizing:border-box;margin:0;padding:0}
  html,body{width:1200px;height:800px;overflow:hidden;background:var(--page);font-family:"Roboto",Arial,sans-serif;color:var(--ink)}
  .sheet{position:absolute;top:40px;width:510px;height:720px;background:var(--white);overflow:hidden;box-shadow:0 6px 20px rgba(0,0,0,.18)}
  .sheet--front{left:55px}
  .sheet--back{left:635px}
  .layer{position:absolute;left:0;top:0}
  .abs{position:absolute}

  /* brand */
  .brand{position:absolute;display:flex;align-items:center;gap:8px;color:var(--red);font-weight:900;line-height:1.02;letter-spacing:.5px}
  .brand__mark{width:30px;height:30px;background:var(--red);flex:none}

  /* front */
  .photo-keypad{left:0;top:0;width:330px;height:300px;background:linear-gradient(135deg,#d9dde2 0%,#f2f3f5 55%,#c9ccd1 100%)}
  .photo-phones{left:16px;top:300px;width:250px;height:265px;background:linear-gradient(160deg,#2c3036 0%,#5a6470 45%,#9fb7cf 100%);border-radius:18px}
  .front-brand{right:22px;top:22px;font-size:20px;flex-direction:column;align-items:center;gap:6px;text-align:center}
  .front-brand .brand__mark{width:40px;height:40px}
  .headline{right:22px;top:140px;text-align:right;color:var(--red);font-weight:900;font-size:38px;line-height:1.08;letter-spacing:.5px}
  .price-intro{right:22px;top:222px;font-size:17px;font-weight:400;color:#333;display:flex;align-items:center;gap:8px}
  .price-intro::after{content:"";width:60px;height:1px;background:#888}
  .price-main{right:22px;top:240px;font-size:34px;font-weight:700;color:var(--ink)}
  .cctv{left:278px;top:290px;width:220px}
  .cctv__title{font-size:29px;font-weight:400;color:#222}
  .cctv__price{font-size:17px;font-weight:700;color:var(--red);margin-top:2px}
  .cctv__note{font-size:17px;font-weight:400;color:#333}
  .takeover{left:252px;top:374px;width:258px;height:134px;background:var(--black);padding:12px 0 0 20px;color:var(--white)}
  .takeover__q1{font-size:17px;font-weight:400}
  .takeover__q2{font-size:19px;font-weight:700;color:var(--yellow)}
  .takeover__body{font-size:14.5px;margin-top:5px;line-height:1.15}
  .takeover__body small{font-size:12px;display:block}
  .takeover__offer{font-size:28px;font-weight:900;color:var(--yellow);line-height:1.1}
  .discount{left:278px;top:514px;width:230px}
  .discount__big{font-size:28px;font-weight:900;color:var(--red);line-height:1}
  .discount__sub{font-size:27px;font-weight:400;color:#222;line-height:1.05}
  .discount__terms{font-size:6px;color:#777}
  .promise{left:0;top:582px;width:510px;height:52px;background:linear-gradient(180deg,var(--red),var(--red-dark));color:var(--white);text-align:center;font-size:14.5px;line-height:1.3;padding-top:8px}
  .promise strong{font-weight:500}
  .contact-row{left:0;top:634px;width:510px;height:60px;display:flex;align-items:center;justify-content:space-between;padding:0 28px 0 30px}
  .cta{background:var(--red);color:var(--white);border-radius:22px;padding:6px 16px;font-size:21px;font-weight:500;box-shadow:0 2px 4px rgba(0,0,0,.3)}
  .phone{display:flex;align-items:center;gap:6px;font-family:"Roboto Condensed",Arial Narrow,sans-serif;font-weight:700;font-size:46px;letter-spacing:-.5px;color:var(--black)}
  .phone svg{width:22px;height:26px}
  .footer{left:0;top:694px;width:510px;height:26px;background:var(--black);color:#ddd;font-size:7px;display:flex;align-items:center;justify-content:center;gap:14px}
  .footer span{display:flex;align-items:center;gap:3px}
  .footer svg{width:8px;height:8px}

  /* back */
  .back-heading{left:24px;top:22px;font-size:22px;line-height:1.4;color:var(--white);font-weight:400}
  .back-heading em{font-style:normal;color:var(--yellow);font-weight:500}
  .back-brand{left:368px;top:22px;width:140px;font-size:16px;flex-direction:column;text-align:center;gap:6px}
  .benefits{left:48px;top:160px;width:440px;list-style:none}
  .benefits li{display:flex;gap:14px;margin-bottom:10px;min-height:36px;font-size:11.6px;font-weight:500;line-height:1.32;text-align:justify;color:var(--ink)}
  .benefits li span.num{flex:none;width:26px;height:26px;background:var(--red);color:var(--white);font-weight:700;font-size:16px;display:flex;align-items:center;justify-content:center;border-radius:2px;margin-top:2px}
  .badges{left:240px;top:538px;width:220px;height:64px}
  .back .contact-row{top:625px;padding:0 28px 0 30px}
  .back .cta{background:var(--red-dark)}
  .back .phone{color:var(--white)}
</style>
</head>
<body>

<!-- Front side -->
<section class="sheet sheet--front" aria-label="Flyer front">
  <div class="abs photo-keypad" role="img" aria-label="Photo of a hand pressing an alarm keypad showing Welcome Home"></div>
  <svg class="layer" width="510" height="720" viewBox="0 0 510 720" aria-hidden="true">
    <path d="M340 0 H510 V300 H300 C285 210 280 70 340 0 Z" fill="#ffffff"/>
    <path d="M0 302 C150 270 330 255 510 282 V300 H0 Z" fill="#ffffff"/>
    <path d="M0 330 C140 285 330 262 510 282 V290 C330 276 150 300 0 352 Z" fill="#d71f26"/>
    <path d="M0 322 C140 278 330 254 510 274 V282 C330 262 140 285 0 330 Z" fill="#3a3a3a"/>
    <rect x="0" y="352" width="510" height="230" fill="#ffffff"/>
    <path d="M0 352 C150 300 330 276 510 290 V310 C330 300 150 320 0 360 Z" fill="#ffffff"/>
  </svg>
  <div class="abs photo-phones" role="img" aria-label="Two smartphones showing a home security control app"></div>

  <div class="brand front-brand"><span class="brand__mark"></span><span>K P GUARD<br>SERVICES</span></div>
  <h1 class="abs headline">INTRUDER<br>ALARMS</h1>
  <div class="abs price-intro">Starting from</div>
  <div class="abs price-main">£495 + VAT</div>

  <div class="abs cctv">
    <div class="cctv__title">CCTV systems</div>
    <div class="cctv__price">Starting from £595 + VAT</div>
    <div class="cctv__note">(based on 2 cameras)</div>
  </div>

  <div class="abs takeover">
    <div class="takeover__q1">NOT HAPPY WITH YOUR</div>
    <div class="takeover__q2">CURRENT PROVIDER?</div>
    <div class="takeover__body">Free of charge no obligation<small>take over survey and quotation and</small></div>
    <div class="takeover__offer">up to £100 off</div>
  </div>

  <div class="abs discount">
    <div class="discount__big">£150 discount</div>
    <div class="discount__sub">On installations</div>
    <div class="discount__terms">*terms and conditions apply</div>
  </div>

  <div class="abs promise">K P Guard Services are always there, always available,<br><strong>wherever and whenever you need us.</strong></div>

  <div class="abs contact-row">
    <span class="cta">Get In Touch</span>
    <span class="phone"><svg viewBox="0 0 24 28"><path d="M6 2 L10 8 L7 11 C8 15 11 19 14 21 L17 18 L22 23 L18 27 C10 25 2 15 2 6 Z" fill="currentColor"/></svg>01632 480913</span>
  </div>

  <div class="abs footer">
    <span><svg viewBox="0 0 10 10"><circle cx="5" cy="4" r="3" fill="none" stroke="#ddd"/></svg>14 Hawthorn Lane, Brentwood, Essex, CM15 9QX</span>
    <span><svg viewBox="0 0 10 10"><rect x="1" y="2" width="8" height="6" fill="none" stroke="#ddd"/></svg>operations@kpguardservices.co.uk</span>
    <span><svg viewBox="0 0 10 10"><circle cx="5" cy="5" r="4" fill="none" stroke="#ddd"/></svg>www.kpguardservices.co.uk</span>
  </div>
</section>

<!-- Back side -->
<section class="sheet sheet--back back" aria-label="Flyer back">
  <svg class="layer" width="510" height="720" viewBox="0 0 510 720" aria-hidden="true">
    <path d="M0 0 H510 V60 C420 80 300 112 170 100 C90 94 40 104 0 116 Z" fill="#111111"/>
    <path d="M0 80 C70 76 130 92 200 98 C320 106 420 80 510 68 V84 C420 102 320 128 200 124 C120 120 60 112 0 128 Z" fill="#d71f26"/>
    <circle cx="437" cy="58" r="76" fill="#ffffff"/>
    <path d="M0 552 C150 600 350 592 510 532 V545 C350 600 150 610 0 566 Z" fill="#111111"/>
    <path d="M0 566 C150 612 350 602 510 545 V694 H0 Z" fill="#d71f26"/>
  </svg>

  <h2 class="abs back-heading">Are you looking to keep<br><em>you and your premises safe?</em></h2>
  <div class="brand back-brand"><span class="brand__mark"></span><span>K P GUARD<br>SERVICES</span></div>

  <ol class="abs benefits">
    <li><span class="num">1</span><span>K P Guard Services install, maintain and repair all intruder alarms, CCTV, intercom and access control</span></li>
    <li><span class="num">2</span><span>View, control and manage your security systems anywhere in the world</span></li>
    <li><span class="num">3</span><span>Feel at ease with monitoring services &amp; police response tailored to suit you and your business</span></li>
    <li><span class="num">4</span><span>K P Guard can takeover any existing security system and offer maintenance checks to guarantee the best performance for you and your premises</span></li>
    <li><span class="num">5</span><span>K P Guard understand that being security conscious is ever increasing, protecting your property and family is a number one priority</span></li>
    <li><span class="num">6</span><span>Our fully insured and accredited team offer quality, safety and cost efficiency throughout the whole process</span></li>
    <li><span class="num">7</span><span>K P Guard Services are using the latest cloud-based technology to stay connected with your home and business 24/7</span></li>
    <li><span class="num">8</span><span>If you are looking to improve the security in your home, office or commercial property then call a member of our team today for a free quote.</span></li>
  </ol>

  <svg class="abs badges" viewBox="0 0 220 64" role="img" aria-label="Accreditation badges: Jobrater member, NQRB intruder alarm and CCTV certification">
    <rect x="0" y="22" width="50" height="14" rx="3" fill="#d71f26" opacity=".8"/>
    <rect x="69" y="0" width="88" height="60" fill="#ffffff" stroke="#6b6b6b"/>
    <circle cx="92" cy="20" r="14" fill="none" stroke="#1d3c78" stroke-width="2"/>
    <rect x="122" y="6" width="28" height="32" fill="none" stroke="#1d3c78" stroke-width="2"/>
    <circle cx="192" cy="20" r="14" fill="none" stroke="#1d3c78" stroke-width="2"/>
  </svg>

  <div class="abs contact-row">
    <span class="cta">Get In Touch</span>
    <span class="phone"><svg viewBox="0 0 24 28"><path d="M6 2 L10 8 L7 11 C8 15 11 19 14 21 L17 18 L22 23 L18 27 C10 25 2 15 2 6 Z" fill="currentColor"/></svg>01632 480913</span>
  </div>

  <div class="abs footer">
    <span><svg viewBox="0 0 10 10"><circle cx="5" cy="4" r="3" fill="none" stroke="#ddd"/></svg>14 Hawthorn Lane, Brentwood, Essex, CM15 9QX</span>
    <span><svg viewBox="0 0 10 10"><rect x="1" y="2" width="8" height="6" fill="none" stroke="#ddd"/></svg>operations@kpguardservices.co.uk</span>
    <span><svg viewBox="0 0 10 10"><circle cx="5" cy="5" r="4" fill="none" stroke="#ddd"/></svg>www.kpguardservices.co.uk</span>
  </div>
</section>

</body>
</html>
```